creating a certificate for our flagship course

Hi,
We need a new certificate for our flagship course called Bright Harbour. We have been running this course for 25 years this year and want to get something special that represents that. We need our logos incorporated and we love to have a compass or Koru incorporated in the certificate. We like something different from your standard certificate, but not too crazy.

The text should say something along the lines of:
This certificate is awarded to ....
For successfully completing and contributing to the three day Bright Harbour programme.

signed:... date:...

to learn a bit more about this course and our company, please check our website. www.hollisvantreeve.co.nz

Thank you!

Target Market(s)

attendees who completed our 3 day programme.

Requirements
Must have
• Both our BH logo and our brand logo. a compass or a koru.
• a 25th year existence something on it.

```html
<!DOCTYPE html>
<html lang="en">
<head>
<meta charset="utf-8">
<title>Certificate of Completion – Bright Harbour</title>
<link rel="stylesheet" href="https://fonts.googleapis.com/css2?family=Arimo&family=Cinzel:wght@500&family=Great+Vibes&family=Open+Sans&family=Pinyon+Script&family=Tinos&display=swap">
<style>
  :root {
    --paper: #ffffff;
    --ink: #111111;
    --brand-navy: #2f2d3c;
    --brand-green: #8dc63f;
    --band-green: #95c83e;
    --band-grey: #bcbec0;
    --band-tan: #c9a06e;
    --numeral-green: #c5e093;
    --rule-grey: #8a8a8a;
    --label-grey: #777777;
  }
  * { margin: 0; padding: 0; box-sizing: border-box; }
  html, body { width: 1200px; height: 927px; overflow: hidden; background: var(--paper); }
  .certificate { position: relative; width: 1200px; height: 927px; background: var(--paper); overflow: hidden; }

  .corner-bands { position: absolute; inset: 0; width: 1200px; height: 927px; }

  .anniversary-numeral {
    position: absolute; left: 850px; top: 20px;
    font-family: "Great Vibes", cursive; font-size: 230px; line-height: 1;
    color: var(--numeral-green); transform: rotate(42deg); transform-origin: left top;
    white-space: nowrap;
  }
  .anniversary-numeral sup { font-family: "Open Sans", sans-serif; font-size: 38px; vertical-align: 110px; }
  .anniversary-line {
    position: absolute; left: 772px; top: 108px;
    font-family: "Open Sans", sans-serif; font-size: 23px; color: var(--paper);
    transform: rotate(42deg); transform-origin: left top; white-space: nowrap;
  }

  .brand { position: absolute; left: 113px; top: 104px; }
  .brand-square { width: 92px; height: 92px; background: var(--brand-green); }
  .brand-name {
    margin-top: 12px; font-family: "Cinzel", serif; font-weight: 500;
    font-size: 40px; line-height: 36px; color: var(--brand-navy); letter-spacing: 2px;
  }
  .brand-name small { font-size: 20px; letter-spacing: 0; }

  .title {
    position: absolute; left: 0; right: 0; top: 345px; text-align: center;
    font-family: "Pinyon Script", cursive; color: var(--ink); white-space: nowrap;
  }
  .title .main { font-size: 96px; }
  .title .rest { font-size: 62px; }

  .awarded, .reason {
    position: absolute; left: 0; right: 0; text-align: center;
    font-family: "Tinos", serif; font-size: 27px; color: var(--ink);
  }
  .awarded { top: 483px; }
  .reason { top: 612px; line-height: 36px; }
  .name-line { position: absolute; left: 322px; width: 556px; top: 581px; border-top: 1px dashed var(--rule-grey); }

  .programme { position: absolute; left: 0; right: 0; top: 703px; text-align: center; }
  .programme-square { width: 68px; height: 68px; margin: 0 auto; background: var(--band-green); }
  .programme-name { margin-top: 5px; font-family: "Arimo", sans-serif; font-size: 23px; color: var(--brand-navy); }

  .sign-field { position: absolute; top: 827px; width: 198px; border-top: 1px solid var(--rule-grey); text-align: center;
    font-family: "Arimo", sans-serif; font-size: 17px; color: var(--label-grey); padding-top: 3px; }
  .sign-field.date { left: 206px; }
  .sign-field.signature { left: 767px; }
</style>
</head>
<body>
<main class="certificate">
  <svg class="corner-bands" viewBox="0 0 1200 927" aria-hidden="true">
    <defs>
      <filter id="band-shadow" x="-10%" y="-10%" width="120%" height="120%">
        <feDropShadow dx="-4" dy="6" stdDeviation="6" flood-color="#000" flood-opacity="0.25"/>
      </filter>
    </defs>
    <polygon fill="var(--band-tan)" points="835,275 1040,385 1200,532 1200,672"/>
    <polygon fill="var(--band-grey)" filter="url(#band-shadow)" points="340,0 1200,0 1200,532 1040,388"/>
    <polygon fill="var(--band-green)" filter="url(#band-shadow)" points="592,0 1200,0 1200,532"/>
  </svg>

  <div class="anniversary-numeral">25<sup>TH</sup></div>
  <div class="anniversary-line">years existence something on it.</div>

  <div class="brand">
    <div class="brand-square"></div>
    <div class="brand-name">HOLLIS<br>VANTREEVE <small>&amp; Associates</small></div>
  </div>

  <h1 class="title"><span class="main">Certificate</span> <span class="rest">of Completion</span></h1>
  <p class="awarded">This certificate is awarded to</p>
  <div class="name-line"></div>
  <p class="reason">For successfully completing and contributing<br>to the three day Bright Harbour programme.</p>

  <div class="programme">
    <div class="programme-square"></div>
    <div class="programme-name">Bright Harbour</div>
  </div>

  <div class="sign-field date">DATE</div>
  <div class="sign-field signature">SIGNATURE</div>
</main>
</body>
</html>
```